Unique Beautiful Realtor business card

I need a unique business card that includes my logo, my firms logo, my picture and phone number. The colors should compliment my logo.

Target Market(s)

People who want to buy or sell a home in South Florida

Contact Information for Business Card

Use two sides and work with the DRM Coastal Homes logo as a theme.
The Harlow Benton should be small and discreet, it is a requirement to be there but should be small. My photo should be integrated artistically.

Font styles to use
Serif
Sans Serif

Colors

Designer to choose colors to be used in the design.

Requirements
Must have
• My logo, Harlow Benton logo, my photo, my phone number, (954-283-6091) and my website address. (www.drmcoastalhomes.example)
• Also my name, Dana R. Moreland, PA, Realtor
• Also “The Pet Friendly Realtor”

```html
<!DOCTYPE html>
<html lang="en">
<head>
<meta charset="utf-8">
<title>Dana R. Moreland – Business Card</title>
<link rel="stylesheet" href="https://fonts.googleapis.com/css2?family=Roboto:wght@400;500;700&family=Roboto+Condensed:ital,wght@1,500&display=swap">
<style>
  :root {
    --navy: #0b4a8b;
    --sky: #1a9ad6;
    --sun: #f5d000;
    --ink: #555a60;
    --paper: #ffffff;
    --backdrop: #e4e4e4;
    --firm: #c21f45;
  }
  * { box-sizing: border-box; margin: 0; padding: 0; }
  html, body { width: 1200px; height: 1200px; overflow: hidden; }
  body {
    background: var(--backdrop);
    font-family: "Roboto", Arial, sans-serif;
    position: relative;
  }
  .card {
    position: absolute;
    left: 240px;
    width: 720px;
    height: 412px;
    background: var(--paper);
    overflow: hidden;
  }
  .card--front { top: 150px; }
  .card--back { top: 640px; }

  /* brand mark */
  .brand {
    display: flex;
    align-items: center;
    gap: 10px;
    white-space: nowrap;
  }
  .brand__dot {
    width: 20px; height: 20px;
    border-radius: 50%;
    background: var(--sun);
    flex: none;
  }
  .brand__name {
    font-weight: 700;
    color: var(--navy);
    letter-spacing: 0.4px;
  }
  .card--front .brand { position: absolute; right: 48px; top: 118px; }
  .card--front .brand__name { font-size: 30px; }

  /* front details */
  .agent {
    position: absolute;
    left: 48px;
    top: 276px;
    right: 36px;
  }
  .agent__name {
    font-size: 29px;
    font-weight: 700;
    color: var(--navy);
    line-height: 1.05;
  }
  .agent__title {
    font-size: 19px;
    color: var(--sky);
    margin-left: 2px;
    line-height: 1.25;
  }
  .contact {
    margin-top: 12px;
    font-size: 15.5px;
    color: var(--ink);
    white-space: nowrap;
  }
  .contact b { color: var(--navy); font-weight: 700; }
  .tagline {
    margin-top: 10px;
    font-family: "Roboto Condensed", "Arial Narrow", sans-serif;
    font-style: italic;
    font-weight: 500;
    font-size: 18px;
    color: var(--navy);
  }
  .band {
    position: absolute;
    left: 0; right: 0; bottom: 0;
    height: 13px;
    background: var(--navy);
  }

  /* back details */
  .portrait {
    position: absolute;
    left: 0;
    top: 18px;
    width: 340px;
    height: 394px;
    background: radial-gradient(ellipse at 46% 30%, #d9b99a 0%, #b89570 22%, #5b5c60 52%, #3f4044 100%);
    border-radius: 48% 48% 0 0 / 30% 30% 0 0;
  }
  .back-info {
    position: absolute;
    left: 370px;
    right: 48px;
    top: 0;
    bottom: 0;
    display: flex;
    flex-direction: column;
    align-items: flex-end;
  }
  .firm {
    margin-top: 44px;
    font-size: 13px;
    font-weight: 500;
    color: var(--firm);
    letter-spacing: 0.3px;
    white-space: nowrap;
  }
  .card--back .brand { margin-top: auto; }
  .card--back .brand__name { font-size: 24px; }
  .web {
    margin-top: 26px;
    margin-bottom: 30px;
    font-size: 15px;
    letter-spacing: 1.5px;
    color: var(--ink);
    white-space: nowrap;
  }
</style>
</head>
<body>

<section class="card card--front">
  <div class="brand">
    <span class="brand__dot"></span>
    <span class="brand__name">DRM Coastal Homes</span>
  </div>

  <div class="agent">
    <h1 class="agent__name">Dana R. Moreland, PA</h1>
    <p class="agent__title">Realtor</p>
    <p class="contact"><b>P:</b> (954-283-6091) <b>E:</b> info@drmcoastalhomes.example <b>W:</b> www.drmcoastalhomes.example</p>
    <p class="tagline">The Pet Friendly Realtor</p>
  </div>
  <div class="band"></div>
</section>

<section class="card card--back">
  <div class="portrait" role="img" aria-label="Portrait photo of the realtor in a grey blazer"></div>
  <div class="back-info">
    <p class="firm">Harlow Benton Realty</p>
    <div class="brand">
      <span class="brand__dot"></span>
      <span class="brand__name">DRM Coastal Homes</span>
    </div>
    <p class="web">www.drmcoastalhomes.example</p>
  </div>
</section>

</body>
</html>
```